VEXA New York *Luxury Candles*

We need a logo AND package design for a new private label luxury candle company.
I'm an interior decorator. When you enter a space you can perceive design as a 3 dimensional experience. However, the perfect scent in a space makes your experience unforgettable and 4 dimensional. Scents have the power to evoke pleasure and bring back memories.
I want my costumer to have a luxurious experience from the moment they see the package, open it, smell, enjoy and use it to decorate their spaces.
We are looking for a clean design that reads LUX. I'm attaching some pictures for Inspiration.
The candle is approximately 4 inches high 3.5 inches wide (10.3cm high, 9cm wide).

The company's name is

VEXA
New York

Target Market(s)

Women between 27 and 50 who like design, elegance, and beautiful spaces.
They like to indulge and create their safety sanctuary at home.

Industry/Entity Type

It Company

Font styles to use
Sans Serif
Script

Requirements
Must have
• A design for the candle and a design for the gift box + logo
Nice to have
• Simplicity
• Elegance
• Efortless beauty
Should not have
• Many different colors
• Shouldn't be overdone

```html
<!DOCTYPE html>
<html lang="en">
<head>
<meta charset="utf-8">
<title>Vexa – Gift Box Face</title>
<link href="https://fonts.googleapis.com/css2?family=Great+Vibes&display=swap" rel="stylesheet">
<style>
  :root {
    --bg: #d9dadc;
    --navy-deep: #0b1d52;
    --navy-mid: #1c477f;
    --navy-edge: #10296a;
    --navy-glow: rgba(44, 92, 160, 0.55);
    --gold: #d9a93a;
    --gold-soft: rgba(217, 169, 58, 0.28);
  }
  html, body {
    margin: 0;
    padding: 0;
    width: 1200px;
    height: 900px;
    overflow: hidden;
    background: var(--bg);
  }
  .canvas {
    width: 1200px;
    height: 900px;
    display: flex;
    align-items: center;
    justify-content: center;
  }
  .box-face {
    position: relative;
    width: 700px;
    height: 600px;
    background: radial-gradient(ellipse 70% 60% at 50% 32%, var(--navy-mid) 0%, var(--navy-edge) 60%, var(--navy-deep) 100%);
    overflow: hidden;
  }
  .brand-name {
    position: absolute;
    top: 150px;
    left: 0;
    right: 0;
    margin: 0;
    text-align: center;
    font-family: "Great Vibes", cursive;
    font-weight: 400;
    font-size: 104px;
    line-height: 1;
    color: var(--gold);
  }
  .star-field {
    position: absolute;
    left: 0;
    right: 0;
    top: 360px;
    height: 190px;
    background:
      radial-gradient(ellipse 60% 40% at 50% 100%, var(--gold-soft) 0%, rgba(217, 169, 58, 0) 100%),
      linear-gradient(to bottom, rgba(44, 92, 160, 0) 0%, var(--navy-glow) 100%);
  }
  .gold-rule {
    position: absolute;
    left: 0;
    right: 0;
    top: 556px;
    height: 4px;
    background: var(--gold);
  }
</style>
</head>
<body>
  <main class="canvas">
    <section class="box-face">
      <h1 class="brand-name">Vexa</h1>
      <div class="star-field" role="img" aria-label="Scattered small gold and silver stars across the lower part of the box"></div>
      <div class="gold-rule"></div>
    </section>
  </main>
</body>
</html>
```